Verelin Publishing

I made a website myself www.verelinpublishing.co.uk a few years ago but I need a new design, which I will code. One that I can be proud of, that 's sexy, to win new customers and showcase my publishing skills. This is a publishing website so I want the home page and books page to be fantastic. I have a logo already so will like the same colour scheme or thereabouts. I have current files and features that I would like to add to your creativity and experience.

Target Market(s)

Web Designers, Graphic Designers

Industry/Entity Type

Book Publisher

Number of Pages Required

5+ page

Font styles to use
Sans Serif

Colors
0255a3
ffffff
ec1f27

Requirements
Must have
• Menu and Sub Menu
• Footer
• Buy Page - Shopping Cart
• Upload feature on the submissions page
• video section on home page (how we publish books)
• Ad space section
Nice to have
• social media bar
• Zoom in page

```html
<!DOCTYPE html>
<html lang="en">
<head>
<meta charset="utf-8">
<title>Verelin Publishing — Home</title>
<link rel="stylesheet" href="https://fonts.googleapis.com/css2?family=Open+Sans:wght@300;400;600&display=swap">
<style>
  :root {
    --brand-blue: #0255a3;
    --brand-red: #ec1f27;
    --white: #ffffff;
    --header-bg: #f4f4f4;
    --nav-text: #3a3a3a;
    --muted: #8a8a8a;
    --icon-grey: #9aa3ad;
    --contact-green: #7cbf3a;
  }
  * { box-sizing: border-box; margin: 0; padding: 0; }
  html, body { width: 1200px; height: 663px; overflow: hidden; background: var(--white); }
  body { font-family: "Open Sans", Arial, sans-serif; }

  .site { position: relative; width: 1200px; height: 663px; }

  .site-header {
    position: absolute; inset: 0 0 auto 0; height: 98px;
    background: var(--header-bg);
    border-bottom: 1px solid #e2e2e2;
  }
  .brand {
    position: absolute; left: 196px; top: 22px;
    display: flex; align-items: center; gap: 8px;
  }
  .brand-mark { width: 14px; height: 14px; border-radius: 50%; background: var(--brand-red); }
  .brand-name {
    font-size: 15px; font-weight: 600; color: var(--brand-blue);
    line-height: 1.15; width: 80px;
  }

  .contact-bar {
    position: absolute; top: 13px; left: 512px;
    display: flex; align-items: center; gap: 26px;
    font-size: 10.5px; color: var(--muted);
  }
  .contact-item { display: flex; align-items: center; gap: 6px; }
  .contact-item svg { display: block; }
  .social-bar { display: flex; gap: 14px; margin-left: 4px; }
  .social-dot { width: 12px; height: 12px; border-radius: 50%; background: var(--icon-grey); }

  .main-nav {
    position: absolute; top: 66px; left: 400px;
    display: flex; gap: 36px;
    font-size: 11px; color: var(--nav-text);
  }
  .main-nav a { color: inherit; text-decoration: none; position: relative; padding-bottom: 12px; }
  .main-nav a.is-active { color: var(--brand-blue); font-weight: 600; }
  .main-nav a.is-active::after {
    content: ""; position: absolute; left: 0; right: 0; bottom: 0;
    height: 2px; background: var(--brand-blue);
  }

  .hero {
    position: absolute; top: 98px; left: 0; width: 1200px; height: 565px;
    overflow: hidden;
  }
  .hero-photo {
    position: absolute; inset: 0;
    background:
      linear-gradient(105deg, rgba(181,150,118,0.85) 0%, rgba(150,140,135,0.55) 35%, rgba(120,140,170,0.2) 60%),
      linear-gradient(180deg, #a99583 0%, #7e8fa7 45%, #5c7598 100%);
  }
  .hero-overlay {
    position: absolute; inset: 0;
    background: linear-gradient(90deg, rgba(40,80,140,0.35) 0%, rgba(40,80,140,0.2) 60%, rgba(40,80,140,0.1) 100%);
  }
  .hero-content {
    position: absolute; left: 419px; top: 145px; transform: translateX(-50%);
    text-align: center; color: var(--white); white-space: nowrap;
  }
  .hero-title { font-size: 45px; font-weight: 400; letter-spacing: 0.2px; }
  .hero-tagline { font-size: 28px; font-weight: 400; margin-top: 10px; }
  .hero-cta {
    display: inline-block; margin-top: 44px;
    width: 270px; height: 56px; line-height: 52px;
    border-radius: 28px; border: 2px solid var(--white);
    background: var(--brand-red); color: var(--white);
    font-size: 21px; font-weight: 400; text-decoration: none;
    box-shadow: 0 2px 6px rgba(0,0,0,0.25);
  }
  .scroll-cue { position: absolute; left: 586px; top: 520px; }
</style>
</head>
<body>
<div class="site">
  <header class="site-header">
    <div class="brand">
      <span class="brand-mark"></span>
      <span class="brand-name">Verelin Publishing</span>
    </div>

    <div class="contact-bar">
      <span class="contact-item">
        <svg width="10" height="10" viewBox="0 0 10 10"><path d="M2 0.5 L3.6 2.6 L2.7 3.6 C3.3 5 4.7 6.4 6.2 7.1 L7.2 6.2 L9.4 7.8 L8.3 9.4 C4.4 9.2 0.6 5.4 0.5 1.6 Z" fill="var(--contact-green)"/></svg>
        +1 234 555 0182
      </span>
      <span class="contact-item">
        <svg width="11" height="8" viewBox="0 0 11 8"><rect x="0.5" y="0.5" width="10" height="7" fill="var(--contact-green)"/><path d="M0.5 0.5 L5.5 4.5 L10.5 0.5" fill="none" stroke="#fff" stroke-width="1"/></svg>
        hello@verelinmail.com
      </span>
      <span class="social-bar" aria-label="Social media links">
        <span class="social-dot"></span>
        <span class="social-dot"></span>
        <span class="social-dot"></span>
        <span class="social-dot"></span>
        <span class="social-dot"></span>
      </span>
    </div>

    <nav class="main-nav">
      <a class="is-active" href="#">Home</a>
      <a href="#">Publishing</a>
      <a href="#">Submissions</a>
      <a href="#">Books</a>
      <a href="#">Authors</a>
      <a href="#">Seminars</a>
      <a href="#">Contact Us</a>
    </nav>
  </header>

  <section class="hero">
    <div class="hero-photo" role="img" aria-label="Photo of a smiling author writing on a laptop at home"></div>
    <div class="hero-overlay"></div>
    <div class="hero-content">
      <h1 class="hero-title">Verelin Publishing</h1>
      <p class="hero-tagline">Self-Publishing That Works</p>
      <a class="hero-cta" href="#">SUBMIT BOOK</a>
    </div>
    <svg class="scroll-cue" width="28" height="28" viewBox="0 0 28 28" aria-label="Scroll down">
      <circle cx="14" cy="14" r="12.5" fill="none" stroke="rgba(255,255,255,0.6)" stroke-width="1.2"/>
      <path d="M9 12 L14 17 L19 12" fill="none" stroke="rgba(255,255,255,0.75)" stroke-width="1.4"/>
    </svg>
  </section>
</div>
</body>
</html>
```